Carrying bags for customer visit

I am looking to make a carrying case that can be used to carry small presents, gifts, our brochure (20 inch X20 inch) and sometimes our samples (which are printed circuit boards that have a size of 24X15). The case should look elegant, show our company logo and our slogan "BOARDS ARE OUR CRAFT". You can try to download our logo from our web site www.tarnvolt.com. I want a contemporary and cool feel of the carrying case that can be any materials. I prefer to use recyclable materials that reflects our company's business philosophy of practicing sustanbility. Also I would like to add Chinese name “锦泰电路(东莞)有限公司" in the bag.
Updates

Need extra days to review

Target Market(s)

Corporate customers who will come into contact with our companies

Colors

Designer to choose colors to be used in the design.

Requirements
Must have
• It has to be attractive and people wanting to use them on a regular basis. Therefore, the logo display and our slogan should be subtle. I want the carrying bags not to be very expensive to produce.

```html
<!DOCTYPE html>
<html lang="en">
<head>
<meta charset="utf-8">
<title>Tarnvolt Carrying Bag – Front Panel</title>
<link rel="stylesheet" href="https://fonts.googleapis.com/css2?family=Cinzel:wght@500;600&family=Noto+Sans+SC:wght@400&display=swap">
<style>
  :root {
    --backdrop: #8796ab;
    --frame-dark: #061806;
    --panel-green: #0f3a0c;
    --panel-green-deep: #0b2f09;
    --olive-gold: #b4b21e;
    --slogan-gold: #b29a2a;
    --label-white: #ffffff;
    --brand-green: #0f3a0c;
    --hole: #3b2a2a;
  }
  * { margin: 0; padding: 0; box-sizing: border-box; }
  html, body {
    width: 1200px; height: 1200px; overflow: hidden;
    background: var(--backdrop);
  }
  .canvas { position: relative; width: 1200px; height: 1200px; }
  .bag-front {
    position: absolute; left: 160px; top: 140px;
    width: 880px; height: 920px;
    background: var(--frame-dark);
  }
  .handle-hole {
    position: absolute; top: 36px; width: 18px; height: 18px;
    border-radius: 50%; background: var(--hole);
  }
  .handle-hole.left { left: 270px; }
  .handle-hole.right { left: 530px; }
  .inner-panel {
    position: absolute; left: 45px; top: 85px; right: 75px; bottom: 85px;
    background: linear-gradient(160deg, var(--panel-green) 0%, var(--panel-green-deep) 100%);
  }
  .brand-plate {
    position: absolute; left: 130px; top: 380px;
    width: 540px; height: 250px;
    background: var(--label-white);
    padding: 12px;
  }
  .brand-plate-rule {
    width: 100%; height: 100%;
    border: 6px solid var(--olive-gold);
    display: flex; align-items: center; justify-content: center; gap: 18px;
  }
  .brand-mark { width: 26px; height: 26px; background: var(--brand-green); }
  .brand-name {
    font-family: "Cinzel", serif; font-weight: 600;
    font-size: 64px; letter-spacing: 4px; color: var(--brand-green);
  }
  .slogan {
    position: absolute; left: 130px; top: 652px; width: 540px;
    text-align: center;
    font-family: "Cinzel", serif; font-weight: 500;
    font-size: 30px; letter-spacing: 2px; color: var(--slogan-gold);
  }
  .accent-line {
    position: absolute; left: 0; right: 0; top: 782px; height: 5px;
    background: var(--olive-gold);
  }
  .company-label {
    position: absolute; left: 160px; top: 752px;
    height: 68px; padding: 0 32px;
    background: var(--frame-dark);
    display: flex; align-items: center;
    font-family: "Noto Sans SC", sans-serif; font-weight: 400;
    font-size: 36px; color: var(--label-white); letter-spacing: 2px;
  }
</style>
</head>
<body>
<main class="canvas">
  <section class="bag-front">
    <span class="handle-hole left"></span>
    <span class="handle-hole right"></span>
    <div class="inner-panel" role="img" aria-label="Faint printed circuit trace pattern in dark green across the panel"></div>
    <div class="brand-plate">
      <div class="brand-plate-rule">
        <span class="brand-mark"></span>
        <span class="brand-name">TARNVOLT</span>
      </div>
    </div>
    <p class="slogan">BOARDS ARE OUR CRAFT</p>
    <div class="accent-line"></div>
    <div class="company-label">锦泰电路(东莞)有限公司</div>
  </section>
</main>
</body>
</html>
```